Website redesign

We need a bold revamp of our website (http://www.brantwoodpower.co.nz/)
which at the moment looks dated. We want a crisp, fresh and bold look. The background image behind web page can go. Open to complete new layout

Target Market(s)

Electrical contracting company- working in the domestic and commercial field

Coding

Coded - Design and coding required

Number of Pages Required

5+ page

Font styles to use
Sans Serif

Colors

Designer to choose colors to be used in the design.

```html
<!DOCTYPE html>
<html lang="en">
<head>
<meta charset="utf-8">
<title>Brantwood Power — Electrical and Maintenance</title>
<link rel="stylesheet" href="https://fonts.googleapis.com/css2?family=Barlow+Semi+Condensed:wght@400;500;600&family=Roboto:wght@400;500;700&display=swap">
<style>
:root{
  --red:#f23b3b;
  --red-dark:#d92d2d;
  --ink:#1d1d1d;
  --text:#555;
  --muted:#888;
  --dark:#2a2120;
  --dark-2:#3a2c29;
  --map:#3d2822;
  --footer:#1a1515;
  --white:#fff;
  --light:#f4f4f4;
  --line:#e3e3e3;
}
*{box-sizing:border-box;margin:0;padding:0}
html,body{width:1200px;height:3488px;overflow:hidden}
body{font-family:"Roboto",Arial,sans-serif;color:var(--text);background:var(--white);position:relative}
.heading{font-family:"Barlow Semi Condensed","Arial Narrow",sans-serif;font-weight:500;color:var(--ink);font-size:34px;line-height:38px}
.heading.light{color:var(--white)}
.rule{width:48px;height:4px;background:var(--red);margin-top:18px}
.btn{display:inline-block;background:var(--red);color:var(--white);font-family:"Roboto",Arial,sans-serif;font-size:10px;font-weight:500;letter-spacing:.5px;text-transform:uppercase;text-align:center;line-height:38px;height:38px;box-shadow:0 4px 10px rgba(242,59,59,.35)}
section{position:absolute;left:0;width:1200px;overflow:hidden}

/* header */
.site-header{position:absolute;top:0;left:0;width:1200px;height:102px;background:var(--white);z-index:5;border-bottom:1px solid var(--line)}
.brand{position:absolute;left:240px;top:0;width:167px;height:112px;background:var(--white);box-shadow:0 4px 12px rgba(0,0,0,.12);display:flex;align-items:center;justify-content:center;gap:8px}
.brand-mark{width:14px;height:14px;background:var(--red)}
.brand-name{font-family:"Barlow Semi Condensed",sans-serif;font-weight:600;font-size:24px;color:var(--ink);line-height:24px}
.topbar{position:absolute;right:240px;top:10px;display:flex;gap:30px;font-size:11px;color:var(--ink)}
.topbar span{display:flex;align-items:center;gap:6px}
.nav{position:absolute;right:240px;top:36px;display:flex;height:66px;border-left:1px solid var(--line)}
.nav a{font-size:10px;font-weight:500;color:var(--ink);text-decoration:none;text-transform:uppercase;padding:0 19px;line-height:66px;border-right:1px solid var(--line)}
.nav a.active{border-top:3px solid var(--red);line-height:60px;border-bottom:3px solid var(--red)}

/* hero */
.hero{top:102px;height:384px;background:linear-gradient(90deg,#3a2a27,#5a4642 45%,#3c2d2a)}
.hero-text{position:absolute;top:118px;width:100%;text-align:center;font-family:"Barlow Semi Condensed",sans-serif;font-weight:500;font-size:32px;line-height:37px;color:var(--white)}
.hero .btn{position:absolute;left:537px;top:224px;width:126px}

/* about */
.about{top:486px;height:470px;background:var(--white)}
.about-copy{position:absolute;left:240px;top:60px;width:340px}
.about-copy p{font-size:10.5px;line-height:15px;color:var(--text);margin-top:14px}
.about-copy .rule{margin-bottom:20px}
.about-copy .btn{width:126px;margin-top:28px}
.about-photo{position:absolute;left:672px;top:0;width:528px;height:470px;background:linear-gradient(135deg,#eef0f2,#d9dde2 60%,#c9cdd3)}

/* services */
.services{top:956px;height:663px;background:linear-gradient(90deg,#2c2221,#3c302d 50%,#2a2120)}
.services .title{position:absolute;left:240px;top:62px}
.grid{position:absolute;left:240px;top:63px;width:720px;height:540px}
.cell{position:absolute;width:180px;height:178px;background:var(--white);display:flex;flex-direction:column;align-items:center;justify-content:center;gap:10px;font-size:13px;color:var(--ink);text-align:center;border:1px solid #eee}
.cell.faint{background:linear-gradient(135deg,#f2f2f2,#e4e4e4)}
.cell svg{width:40px;height:40px}
.cell.featured{background:var(--red);color:var(--white)}
.cell.featured .sub{font-size:9px;opacity:.9}
.cell.featured .more{font-size:8px;font-weight:700;margin-top:14px;letter-spacing:.4px}
.services .btn{position:absolute;left:807px;top:491px;width:124px}

/* projects */
.projects{top:1619px;height:619px;background:#f7f7f7}
.projects .plan{position:absolute;left:0;top:0;width:530px;height:619px;background:linear-gradient(135deg,#ececec,#f8f8f8)}
.projects .title{position:absolute;left:240px;top:56px}
.arrows{position:absolute;right:242px;display:flex;gap:9px}
.arrows span{width:38px;height:38px;display:flex;align-items:center;justify-content:center;background:var(--white);border:1px solid #ccc}
.arrows span.on{background:var(--red);border-color:var(--red)}
.projects .arrows{top:116px}
.card{position:absolute;top:188px;width:349px;height:338px;background:var(--white);box-shadow:0 2px 10px rgba(0,0,0,.08)}
.card .photo{height:249px}
.card h3{font-size:13px;font-weight:500;color:var(--ink);margin:20px 20px 8px}
.card p{font-size:10px;line-height:14px;color:var(--text);margin:0 20px}

/* testimonials */
.testimonials{top:2238px;height:495px;background:linear-gradient(90deg,#1e1818,#2e2524 50%,#1e1818)}
.testimonials .title{position:absolute;left:240px;top:56px}
.testimonials .arrows{top:116px}
.quote{position:absolute;left:240px;top:230px;width:720px;height:202px;background:var(--white);text-align:center;padding:66px 60px 0}
.quote p{font-size:10.5px;line-height:15px;color:var(--text)}
.quote .who{color:var(--red);font-size:13px;margin-top:18px}
.quote .role{font-size:9px;color:var(--muted);margin-top:4px}
.avatar{position:absolute;left:552px;top:182px;width:96px;height:96px;border-radius:50%;background:linear-gradient(#8b8f97,#4a4f58);border:4px solid var(--white);z-index:2}

/* contact */
.contact{top:2733px;height:374px;background:var(--white)}
.contact .photo{position:absolute;left:670px;top:0;width:530px;height:374px;background:linear-gradient(135deg,#f4f4f4,#e2e2e2)}
.contact .title{position:absolute;left:240px;top:60px}
.contact-card{position:absolute;left:240px;top:193px;width:720px;height:170px;background:var(--white);box-shadow:0 2px 14px rgba(0,0,0,.1);display:flex;justify-content:space-around;align-items:flex-start;padding-top:34px}
.contact-item{display:flex;flex-direction:column;align-items:center;gap:12px;font-size:13px;color:var(--ink);text-align:center;line-height:16px}
.contact-item svg{width:38px;height:38px}
.phones div{display:flex;gap:8px;align-items:center;font-size:13px}

/* map & footer */
.map{top:3107px;height:319px;background:linear-gradient(135deg,#4a3029,#3a241f 50%,#45302a)}
.site-footer{position:absolute;top:3426px;left:0;width:1200px;height:62px;background:var(--footer);color:#ddd;font-size:10px;display:flex;align-items:center;justify-content:center;gap:6px}
.site-footer .accent{color:var(--red)}
</style>
</head>
<body>

<header class="site-header">
  <div class="brand"><span class="brand-mark"></span><span class="brand-name">Brantwood Power</span></div>
  <div class="topbar">
    <span><svg width="9" height="12" viewBox="0 0 9 12"><rect x="1" y="0.5" width="7" height="11" rx="1.2" fill="none" stroke="#f23b3b"/></svg>0800 55 10 42</span>
    <span><svg width="11" height="11" viewBox="0 0 24 24"><path d="M6.6 10.8a15 15 0 0 0 6.6 6.6l2.2-2.2c.3-.3.7-.4 1-.2 1.1.4 2.3.6 3.6.6.6 0 1 .4 1 1V20c0 .6-.4 1-1 1A17 17 0 0 1 3 4c0-.6.4-1 1-1h3.5c.6 0 1 .4 1 1 0 1.3.2 2.5.6 3.6.1.3 0 .7-.2 1z" fill="#f23b3b"/></svg>(06) 555 0172</span>
  </div>
  <nav class="nav">
    <a class="active" href="#">Home</a><a href="#">About Us</a><a href="#">Services</a><a href="#">Projects</a><a href="#">Contact Us</a>
  </nav>
</header>

<section class="hero" role="img" aria-label="Electrician at work, dark warm toned photograph">
  <h1 class="hero-text">Leading Electrical and Maintenance<br>servicing all of New Zealand.</h1>
  <a class="btn" href="#">Get a quote</a>
</section>

<section class="about">
  <div class="about-copy">
    <h2 class="heading">About<br>Brantwood Power</h2>
    <div class="rule"></div>
    <p>Brantwood Power is a leading electrical installation and maintenance company based in Brantwood, but servicing all New Zealand.</p>
    <p>With over 15 professionally qualified and experienced Brantwood electricians, technicians and support staff we are leading the way in providing quality electrical services.</p>
    <p>Brantwood Power was established in 1961 and does it all; from supplying and changing light bulbs, comprehensive whole house electrical design and installation, to commercial and large scale industrial consultation, implementation and servicing.</p>
    <a class="btn" href="#">Learn more</a>
  </div>
  <div class="about-photo" role="img" aria-label="Smiling electrician in hard hat and tool belt"></div>
</section>

<section class="services">
  <h2 class="heading light title">Our<br>Services</h2>
  <div class="rule" style="position:absolute;left:240px;top:138px"></div>
  <div class="grid">
    <div class="cell faint" style="left:180px;top:0">
      <svg viewBox="0 0 40 40" fill="none" stroke="#f23b3b" stroke-width="2"><path d="M12 30V20a8 8 0 0 1 16 0v10"/><rect x="8" y="30" width="24" height="5"/><path d="M20 4v4M8 10l3 3M32 10l-3 3"/></svg>Alarms</div>
    <div class="cell" style="left:360px;top:0">
      <svg viewBox="0 0 40 40" fill="none" stroke="#f23b3b" stroke-width="2"><rect x="5" y="6" width="30" height="28" rx="2"/><circle cx="14" cy="15" r="4"/><circle cx="26" cy="15" r="4"/><circle cx="14" cy="26" r="4"/><circle cx="26" cy="26" r="4"/></svg>Appliances</div>
    <div class="cell faint" style="left:540px;top:0">
      <svg viewBox="0 0 40 40" fill="none" stroke="#f23b3b" stroke-width="2"><path d="M23 4 11 22h9l-3 14 12-18h-9z"/></svg>Electrical</div>
    <div class="cell faint" style="left:0;top:178px">
      <svg viewBox="0 0 40 40" fill="none" stroke="#f23b3b" stroke-width="2"><path d="M20 4c2 7 10 11 10 20a10 10 0 0 1-20 0c0-5 3-8 5-10 0 4 2 6 4 6 0-6-2-10 1-16z"/></svg>Fire / Smoke</div>
    <div class="cell featured" style="left:180px;top:178px">Heat Pumps<span class="sub">Sales / Installation / Servicing</span><span class="more">SEE DETAILS ›</span></div>
    <div class="cell faint" style="left:360px;top:178px">
      <svg viewBox="0 0 40 40" fill="none" stroke="#f23b3b" stroke-width="2"><rect x="6" y="12" width="24" height="20" transform="rotate(-15 18 22)"/><path d="M10 18l8 5 8-7"/><path d="M28 8l6 6-10 10"/></svg>IQP Building<br>Compliance</div>
    <div class="cell" style="left:540px;top:178px">
      <svg viewBox="0 0 40 40" fill="none" stroke="#f23b3b" stroke-width="2"><rect x="12" y="4" width="16" height="32" rx="2"/><path d="M16 18a6 6 0 0 1 8 0M18 21a3 3 0 0 1 4 0"/><circle cx="20" cy="31" r="1"/></svg>Phone / Data</div>
    <div class="cell" style="left:0;top:356px">
      <svg viewBox="0 0 40 40" fill="none" stroke="#f23b3b" stroke-width="2"><path d="M6 12l22 6-3 8-21-6z"/><path d="M14 23l-2 8H6M30 16l4 1-2 6-4-1"/></svg>Security</div>
    <div class="cell faint" style="left:180px;top:356px">
      <svg viewBox="0 0 40 40" fill="none" stroke="#f23b3b" stroke-width="2"><rect x="5" y="8" width="30" height="20" rx="1"/><path d="M14 34h12M20 28v6M12 22l6-6 4 4 6-6"/></svg>TV</div>
  </div>
  <a class="btn" href="#">View all</a>
</section>

<section class="projects">
  <div class="plan" role="img" aria-label="Faint architectural plan drawings"></div>
  <h2 class="heading title">Recent<br>Projects</h2>
  <div class="rule" style="position:absolute;left:240px;top:132px"></div>
  <div class="arrows"><span><svg width="8" height="10" viewBox="0 0 8 10"><path d="M6 1 2 5l4 4" stroke="#333" fill="none" stroke-width="1.6"/></svg></span><span class="on"><svg width="8" height="10" viewBox="0 0 8 10"><path d="M2 1l4 4-4 4" stroke="#fff" fill="none" stroke-width="1.6"/></svg></span></div>
  <article class="card" style="left:240px">
    <div class="photo" role="img" aria-label="Red brick heritage building on a street corner" style="background:linear-gradient(180deg,#9fc3e4 0%,#b9cfe0 25%,#a8513f 45%,#8c3e30 75%,#6d6d6d 100%)"></div>
    <h3>Civic Building - New Build</h3>
    <p>Civic Building - Everything Electrical as well as installation of specialised security system.</p>
  </article>
  <article class="card" style="left:609px">
    <div class="photo" role="img" aria-label="Modern bank branch shopfront with glass facade" style="background:linear-gradient(180deg,#b8c4cc 0%,#8fa3b3 35%,#4a6f92 60%,#7a7e82 85%,#a0a0a0 100%)"></div>
    <h3>Harbour Bank - Re-modeling</h3>
    <p>Harbour Bank New Building Project - Electrical work for building owner.</p>
  </article>
</section>

<section class="testimonials">
  <h2 class="heading light title">What<br>Clients Say</h2>
  <div class="rule" style="position:absolute;left:240px;top:132px"></div>
  <div class="arrows"><span><svg width="8" height="10" viewBox="0 0 8 10"><path d="M6 1 2 5l4 4" stroke="#333" fill="none" stroke-width="1.6"/></svg></span><span class="on"><svg width="8" height="10" viewBox="0 0 8 10"><path d="M2 1l4 4-4 4" stroke="#fff" fill="none" stroke-width="1.6"/></svg></span></div>
  <div class="avatar" role="img" aria-label="Client portrait"></div>
  <div class="quote">
    <p>Lorem ipsum dolor sit amet, consectetuer adipiscing elit, sed diam nonummy nibh euismod tincidunt ut laoreet dolore magna aliquam erat volutpat. Ut wisi enim ad minim veniam, quis nostrud exerci tation ullamcorper suscipit lobortis nisl ut aliquip ex ea commodo consequat.</p>
    <div class="who">Mr. Daniel Reeve</div>
    <div class="role">Position, Company</div>
  </div>
</section>

<section class="contact">
  <div class="photo" role="img" aria-label="Faint photo of a man on the phone"></div>
  <h2 class="heading title">Get<br>In Touch</h2>
  <div class="rule" style="position:absolute;left:240px;top:136px"></div>
  <div class="contact-card">
    <div class="contact-item">
      <svg viewBox="0 0 40 40" fill="none" stroke="#f23b3b" stroke-width="2"><path d="M20 37s11-12 11-21a11 11 0 0 0-22 0c0 9 11 21 11 21z"/><circle cx="20" cy="16" r="4"/></svg>
      <div>14 Larch Street.<br>Brantwood 4510</div>
    </div>
    <div class="contact-item phones">
      <svg viewBox="0 0 40 40" fill="none" stroke="#f23b3b" stroke-width="2"><rect x="8" y="10" width="24" height="26" rx="2"/><path d="M12 10V5h10v5"/><rect x="13" y="15" width="14" height="6"/><path d="M13 26h2M19 26h2M25 26h2M13 31h2M19 31h2M25 31h2"/></svg>
      <div>☏ 0800 55 10 42</div>
      <div>✆ (06) 555 0172</div>
      <div>▤ (06) 555 0173</div>
    </div>
    <div class="contact-item">
      <svg viewBox="0 0 40 40" fill="none" stroke="#f23b3b" stroke-width="2"><rect x="5" y="9" width="30" height="22"/><path d="M5 9l15 12 15-12M5 31l11-10M35 31 24 21"/></svg>
      <div>office@brantwoodpower.co.nz</div>
    </div>
  </div>
</section>

<section class="map" role="img" aria-label="Dark street map of the office surroundings"></section>

<footer class="site-footer">Copyright © 2018 <span class="accent">Brantwood Power</span></footer>

</body>
</html>
```